Buch-/E-Book-Cover
Zielgruppe
Unternehmensberater, Spezialbereiche Sales und Recruiting
Arbeiten mit der Wegweiser Methode
Zielgruppe sind Führungskräfte in der HR- oder Sales-Abteilung
Management consultant, specialising in sales and recruiting
Working with the Wayfinder Method
Target group are managers in the HR or sales department
Aufgabenstellung
Bitte keine Magneten, Zielscheiben, Schiffe etc. Das kommt so oft vor. Es geht um Touchpoints, die aufeinander abgestimmt sind. Wertigkeit, kreative und besondere Dinge.
Buchtitel (NEU!!!!!)
(Autorin) Heike Brandauer
(Subtitel aber darüber) Kunden Kompass Methode (KKM®)
(Haupttitel) Mit Neugier, Gelassenheit und Erfindergeist zu Ihrem Idealkunden.
(Subtitel 2) Alltagserprobte Ideen für Ihren Verkaufserfolg (im Kreis)
– siehe Layout unten das wir für einen anderen Titel schon gemacht hatten –
Format: DIN A6, Taschenguide. Schnell zur Hand und schnell gelesen.
Please no magnets, targets, ships, etc. That happens so often. It's about touchpoints that are coordinated. Value, creative and special things.
Book title (NEW!!!!!)
(Author) Heike Brandauer
(Subtitle but above) Kunden Kompass Methode (KKM®)
(Main title) With joy, ease and creativity to your desired customer.
(Subtitle 2) Proven tips for your sales success (in a circle)
- see layout below which we had already done for another title -
Format: DIN A6, pocket guide. Quickly to hand and quickly read.

```html
<!DOCTYPE html>
<html lang="de">
<head>
<meta charset="utf-8">
<title>Mit Neugier, Gelassenheit und Erfindergeist zu Ihrem Idealkunden</title>
<link href="https://fonts.googleapis.com/css2?family=Khand:wght@300;400;500;600;700&display=swap" rel="stylesheet">
<style>
  :root {
    --coral: #ee7563;
    --cream: #fdf1d6;
    --teal: #3fb8c4;
    --navy: #3e4f7a;
  }
  html, body {
    margin: 0;
    padding: 0;
    overflow: hidden;
    background: var(--coral);
  }
  .cover {
    position: relative;
    width: 858px;
    height: 1200px;
    background: var(--coral);
    color: var(--cream);
    font-family: "Khand", "Arial Narrow", sans-serif;
    overflow: hidden;
  }
  .series {
    position: absolute;
    top: 78px;
    left: 0;
    width: 100%;
    margin: 0;
    text-align: center;
    font-size: 26px;
    font-weight: 600;
    letter-spacing: 0.2px;
  }
  .title {
    position: absolute;
    top: 134px;
    left: 0;
    width: 100%;
    margin: 0;
    text-align: center;
    font-size: 70px;
    line-height: 68px;
    font-weight: 700;
    text-transform: uppercase;
    letter-spacing: 0.5px;
  }
  .artwork {
    position: absolute;
    left: 0;
    top: 420px;
  }
  .badge {
    position: absolute;
    left: 511px;
    top: 704px;
    width: 290px;
    height: 290px;
  }
  .badge svg {
    position: absolute;
    inset: 0;
  }
  .badge-text {
    position: absolute;
    inset: 0;
    margin: 0;
    display: flex;
    align-items: center;
    justify-content: center;
    text-align: center;
    font-size: 34px;
    line-height: 38px;
    font-weight: 400;
  }
  .author {
    position: absolute;
    top: 1090px;
    left: 0;
    width: 100%;
    margin: 0;
    text-align: center;
    font-size: 40px;
    font-weight: 300;
  }
</style>
</head>
<body>
<main class="cover">
  <p class="series">Kunden Kompass Methode (KKM®)</p>
  <h1 class="title">Mit Neugier, Gelassenheit<br>und Erfindergeist zu<br>Ihrem Idealkunden</h1>

  <svg class="artwork" width="530" height="420" viewBox="0 0 530 420" role="img" aria-label="Illustration: eine Hand wirft einen gemalten Pinselkreis">
    <defs>
      <linearGradient id="handTone" x1="0" y1="1" x2="1" y2="0">
        <stop offset="0" stop-color="#3e4f7a"/>
        <stop offset="1" stop-color="#3fb8c4"/>
      </linearGradient>
    </defs>
    <rect x="0" y="0" width="320" height="412" fill="url(#handTone)"/>
    <rect x="338" y="78" width="178" height="172" fill="url(#handTone)"/>
  </svg>

  <div class="badge">
    <svg width="290" height="290" viewBox="0 0 290 290" aria-hidden="true">
      <circle cx="145" cy="145" r="141" fill="none" stroke="var(--cream)" stroke-width="5" stroke-linecap="round" stroke-dasharray="0 11.1"/>
    </svg>
    <p class="badge-text">Alltagserprobte<br>Ideen für Ihren<br>Verkaufserfolg</p>
  </div>

  <p class="author">Heike Brandauer</p>
</main>
</body>
</html>
```